A layout of a webpage for oil trade platform

I would like to have a desgin of one page webpage (with section scrollling dowin) that woulf present the new product i.e. oil trade platform for wholesale buyers and sellers.
Layout should consist of the sections similar to the given at: https://klinika.pewnywybor.pl/system-zarzadzania-wizytami
However oil industy require more colors and more photo stories than here for doctor.
I. I woul imagine at first below menu a slider with brueg information about the product and its advantages with "more" button next to the prict screen of our platform on different displays (PC and mobile).
II. Bellow the slider I would imagine icons correspoing to the advantages of that plaftorm:
1. Purchase/sale process automation 24/7
2. Access to the best deals
3. Electronic offerings and orderings
4. Transaction status monitoring
5. Data and transaction security
II A) (optional):
In near future we would like to prepare a short video presenation. Hence please prepare a place to display that element here.
At the moment alternatvily please prepare a How it works section that would explan the platform operating process
III. Next secion is about benefits for Oil Purchaser
It can be done either by icons of by text and corresponding grahip for while section.
Benefits:
- Access to cheaper oil
- Convenience of online orders
- Possibility to compare prices on the market
- Transaction history
- Order status monitoring
- Seccurity and transparency of purchase
IV. Next seciont is about benefits for Oil Seller
Benefits:
- New sale channel
- Attracting new clients
- More oil sold
- Transaction security
- Possibility to integrate with distribution infrastructure and logistits for more efficient automation.
V. Contact form
VI. Footer
I would need a layout that that will correspond to the very dynamic logo but I would expect also a clean form, smoth and modern. It has to be proffessional layout with more corporate character.
It can use a paralax features if needed.

```html
<!DOCTYPE html>
<html lang="en">
<head>
<meta charset="utf-8">
<title>Crudexa – Oil Trade Platform</title>
<link rel="stylesheet" href="https://fonts.googleapis.com/css2?family=Lato:wght@700;900&family=Open+Sans:wght@400;600;700&display=swap">
<style>
:root{
  --orange:#f05a28;
  --navy:#0d1a3c;
  --ink:#1f1f1f;
  --muted:#555;
  --band:#e5e5e5;
  --white:#fff;
  --hero-a:#3b4a63;
  --hero-b:#6b6f7c;
  --hero-c:#2c3446;
}
*{box-sizing:border-box;margin:0;padding:0}
html,body{width:1200px;height:2748px;overflow:hidden}
body{position:relative;font-family:"Open Sans",Arial,sans-serif;color:var(--ink);background:var(--white)}
.abs{position:absolute}

/* hero */
.hero{left:0;top:0;width:1200px;height:562px;background:linear-gradient(180deg,var(--hero-a) 0%,var(--hero-b) 35%,var(--hero-c) 100%)}
.menu-btn{left:232px;top:18px}
.brand{left:530px;top:30px;display:flex;align-items:center;gap:10px;color:var(--white);font-family:"Open Sans",sans-serif;font-weight:700;font-size:24px;letter-spacing:.5px}
.brand .dot{width:20px;height:20px;border-radius:50%;background:var(--orange)}
.hero-title{left:268px;top:122px;width:470px;font-family:"Lato",sans-serif;font-weight:900;font-size:49px;line-height:54px;color:var(--white)}
.hero-text{left:272px;top:252px;width:456px;font-size:15.5px;line-height:27px;color:var(--white);text-align:center;font-weight:600}
.slide-arrow{top:277px}
.slide-dots{left:444px;top:395px;display:flex;gap:20px}
.slide-dots span{width:7px;height:7px;border-radius:50%;background:#ccc}
.slide-dots span.on{background:var(--orange)}
.btn{height:30px;border-radius:15px;font-size:11px;font-weight:700;display:flex;align-items:center;justify-content:center;color:var(--white);text-transform:uppercase}
.btn-fill{background:var(--orange)}
.btn-line{border:1.5px solid var(--orange)}
.devices{left:715px;top:275px;width:475px;height:293px;background:linear-gradient(135deg,#2a3344,#e9edf2 45%,#1a1d24);border-radius:6px;opacity:.9}
.scroll-mark{left:470px;top:498px;width:14px;height:28px;border:1.5px solid #aaa;border-radius:7px}

/* feature icons */
.feature{top:612px;width:160px;text-align:center}
.feature svg{display:block;margin:0 auto 10px}
.feature p{font-size:13px;font-weight:700;line-height:16px;color:#333}
.play{left:968px;top:610px;width:80px;height:80px;border-radius:50%;background:var(--orange);box-shadow:0 4px 10px rgba(0,0,0,.3)}

/* sections */
.band{left:0;width:1200px;background:var(--band)}
.section-title{left:0;width:1200px;text-align:center;font-weight:700;font-size:30px;color:#111}
.benefit{width:220px;text-align:center}
.benefit svg{display:block;margin:0 auto}
.benefit h3{font-size:13px;font-weight:700;line-height:16px;margin-top:12px;height:34px;display:flex;align-items:center;justify-content:center}
.benefit p{font-size:10.5px;line-height:16px;font-weight:600;margin-top:14px;padding:0 12px}

.drop-deco{left:320px;top:1560px;width:560px;height:480px;background:radial-gradient(ellipse at 50% 70%,rgba(180,185,195,.45) 0%,rgba(200,205,212,.25) 45%,rgba(255,255,255,0) 70%)}
.card{width:167px;height:229px;border:1.5px solid var(--orange);background:rgba(255,255,255,.6);text-align:center;padding-top:14px}
.card svg{display:block;margin:0 auto}
.card h3{font-size:12px;font-weight:700;line-height:14px;margin-top:6px;height:30px;display:flex;align-items:center;justify-content:center}
.card p{font-size:10px;line-height:15px;font-weight:600;margin-top:22px;padding:0 6px}

/* contact */
.contact-lead{left:240px;top:2220px;width:720px;text-align:center;font-size:15px;line-height:30px;font-weight:600;color:var(--muted)}
.address{left:253px;top:2358px;font-size:12px;line-height:20px;font-weight:600}
.address h4{font-size:16px;font-weight:700;margin-bottom:8px}
.info{left:376px;top:2376px;font-size:12px;line-height:24px;font-weight:600}
.info div{display:flex;align-items:center;gap:8px}
.connect{left:300px;top:2512px;width:120px;text-align:center;font-size:13px;color:#333}
.social{top:2554px;width:28px;height:28px;border-radius:50%;background:#5a6678}
.field{left:559px;width:397px;border:1.5px solid var(--orange);background:#eee;font-size:10px;padding:4px 4px;color:#222}
.send{left:559px;top:2640px;width:124px;height:25px;border-radius:13px;background:var(--orange);color:var(--white);font-size:10px;font-weight:700;display:flex;align-items:center;justify-content:center}

.footer{left:0;top:2693px;width:1200px;height:55px;background:var(--navy);color:#4a5878;font-size:12px;display:flex;align-items:center;justify-content:center}
</style>
</head>
<body>

<!-- hero -->
<section class="abs hero" role="img" aria-label="Photo of an offshore oil platform at dusk over the sea"></section>
<svg class="abs menu-btn" width="28" height="20" viewBox="0 0 28 20"><g stroke="#fff" stroke-width="2"><line x1="0" y1="3" x2="18" y2="3"/><line x1="0" y1="10" x2="18" y2="10"/><line x1="0" y1="17" x2="18" y2="17"/></g><path d="M21 9l3 3 3-3z" fill="#fff"/></svg>
<div class="abs brand"><span class="dot"></span>Crudexa</div>
<h1 class="abs hero-title">The best oil we can trade for you today.</h1>
<p class="abs hero-text">Pellentesque aliquet lacus vitae pede. Nullam mollis dolor ac nisi. Phasellus sit amet urna. Praesent pellentesque sapien sed lacus. Donec , vel feugiat ante velit sit amet mauris. Vivamauctor. Suspendisse le, consequat .</p>
<svg class="abs slide-arrow" style="left:200px" width="22" height="26"><path d="M20 2L2 13l18 11z" fill="#fff"/></svg>
<svg class="abs slide-arrow" style="left:730px" width="22" height="26"><path d="M2 2l18 11L2 24z" fill="#fff"/></svg>
<div class="abs slide-dots"><span></span><span class="on"></span><span></span></div>
<a class="abs btn btn-fill" style="left:343px;top:449px;width:115px">Contact us</a>
<a class="abs btn btn-line" style="left:498px;top:449px;width:116px">Discover more</a>
<div class="abs devices" role="img" aria-label="Platform dashboard screenshots on desktop, laptop, tablet and phone"></div>
<div class="abs scroll-mark"></div>

<!-- features -->
<div class="abs feature" style="left:173px">
  <svg width="50" height="50" viewBox="0 0 50 50"><circle cx="25" cy="17" r="11" fill="#3b4a63"/><path d="M6 48c2-13 10-18 19-18s17 5 19 18z" fill="#3b4a63"/><path d="M13 17a12 12 0 0 1 24 0" stroke="var(--orange)" stroke-width="3" fill="none"/></svg>
  <p>Purchase/sales automation 24/7</p></div>
<div class="abs feature" style="left:338px">
  <svg width="50" height="50" viewBox="0 0 50 50"><path d="M4 22l14-12 10 8-8 8zM46 22L32 10l-12 10 12 14z" fill="#3b4a63"/><path d="M16 30l10 10 6-6" stroke="#3b4a63" stroke-width="4" fill="none"/></svg>
  <p>Access to the best deals</p></div>
<div class="abs feature" style="left:495px">
  <svg width="50" height="50" viewBox="0 0 50 50"><circle cx="25" cy="25" r="23" fill="#3b4a63"/><g fill="#fff"><circle cx="18" cy="18" r="4"/><circle cx="32" cy="32" r="4"/></g><line x1="33" y1="15" x2="17" y2="35" stroke="#fff" stroke-width="3"/></svg>
  <p>Electronic offerings and orderings</p></div>
<div class="abs feature" style="left:664px">
  <svg width="66" height="50" viewBox="0 0 66 50"><rect x="2" y="6" width="42" height="28" fill="none" stroke="#3b4a63" stroke-width="3"/><rect x="16" y="34" width="14" height="8" fill="#3b4a63"/><path d="M12 20h18l-5-5M30 20l-5 5" stroke="#3b4a63" stroke-width="3" fill="none"/><g fill="#3b4a63"><ellipse cx="54" cy="16" rx="10" ry="4"/><rect x="44" y="18" width="20" height="6"/><rect x="44" y="26" width="20" height="6"/><rect x="44" y="34" width="20" height="6"/></g></svg>
  <p>Transaction status monitoring</p></div>
<div class="abs feature" style="left:796px">
  <svg width="50" height="50" viewBox="0 0 50 50"><circle cx="25" cy="25" r="23" fill="#3b4a63"/><path d="M25 10l12 5v9c0 8-6 13-12 16-6-3-12-8-12-16v-9z" fill="#fff"/><path d="M25 13v24c5-3 9-7 9-13v-7z" fill="#3b4a63"/></svg>
  <p>Data and transaction security</p></div>
<div class="abs play"><svg width="80" height="80" viewBox="0 0 80 80"><path d="M33 26l20 14-20 14z" fill="#fff"/></svg></div>

<!-- purchaser benefits -->
<section class="abs band" style="top:760px;height:605px"></section>
<h2 class="abs section-title" style="top:782px">Benefits for Oil Purchaser</h2>

<div class="abs benefit" style="left:201px;top:878px">
  <svg width="42" height="42" viewBox="0 0 42 42"><path d="M4 4h16l18 18-16 16L4 20z" fill="var(--orange)"/><circle cx="12" cy="12" r="3" fill="#fff"/><line x1="16" y1="24" x2="26" y2="24" stroke="#fff" stroke-width="3"/></svg>
  <h3>Access to cheaper oil</h3>
  <p>Sed eget turpis a pede tempor malesuada. Vivamus quis mi at leo pulvinar hendrerit. Cum sociis natoque penatibus et magnis dis parturient montes, nascet.</p></div>
<div class="abs benefit" style="left:495px;top:878px">
  <svg width="42" height="42" viewBox="0 0 42 42"><rect x="4" y="4" width="34" height="26" fill="none" stroke="var(--orange)" stroke-width="3"/><rect x="1" y="32" width="40" height="5" fill="var(--orange)"/><path d="M13 12h3l3 9h9l2-7H17" stroke="var(--orange)" stroke-width="2.5" fill="none"/></svg>
  <h3>Convenience of online orders</h3>
  <p>Sed eget turpis a pede tempor malesuada. Vivamus quis mi at leo pulvinar hendrerit. Cum sociis natoque penatibus et magnis dis parturient montes, nascet.</p></div>
<div class="abs benefit" style="left:777px;top:878px">
  <svg width="52" height="42" viewBox="0 0 52 42"><path d="M3 2v38h48" stroke="var(--orange)" stroke-width="2" fill="none"/><path d="M5 38C15 38 14 4 20 4s6 34 30 34" stroke="var(--orange)" stroke-width="2" fill="none"/><path d="M5 38C18 38 18 14 24 14s8 24 26 24" stroke="var(--orange)" stroke-width="2" fill="none"/></svg>
  <h3>Possibility to compare prices on the market</h3>
  <p>Sed eget turpis a pede tempor malesuada. Vivamus quis mi at leo pulvinar hendrerit. Cum sociis natoque penatibus et magnis dis parturient montes.</p></div>

<div class="abs benefit" style="left:201px;top:1132px">
  <svg width="44" height="42" viewBox="0 0 44 42"><path d="M4 2h38l-4 8H8z" fill="var(--orange)"/><path d="M10 12h10l-8 28H4zM24 12h10l-8 28h-8z" fill="var(--orange)"/></svg>
  <h3>Transaction history</h3>
  <p>Sed eget turpis a pede tempor malesuada. Vivamus quis mi at leo pulvinar hendrerit. Cum sociis natoque penatibus et magnis dis parturient montes.</p></div>
<div class="abs benefit" style="left:495px;top:1132px">
  <svg width="50" height="42" viewBox="0 0 50 42"><rect x="6" y="2" width="38" height="26" fill="none" stroke="var(--orange)" stroke-width="2"/><path d="M2 32h46l-3 6H5z" fill="none" stroke="var(--orange)" stroke-width="2"/></svg>
  <h3>Order status monitoring</h3>
  <p>Sed eget turpis a pede tempor malesuada. Vivamus quis mi at leo pulvinar hendrerit. Cum sociis natoque penatibus et magnis dis parturient montes.</p></div>
<div class="abs benefit" style="left:777px;top:1132px">
  <svg width="52" height="46" viewBox="0 0 52 46"><rect x="2" y="8" width="30" height="22" fill="none" stroke="var(--orange)" stroke-width="3"/><rect x="0" y="32" width="34" height="4" fill="var(--orange)"/><circle cx="34" cy="20" r="11" fill="#fff" stroke="var(--orange)" stroke-width="3"/><line x1="42" y1="28" x2="50" y2="36" stroke="var(--orange)" stroke-width="4"/><rect x="29" y="19" width="10" height="8" fill="var(--orange)"/><path d="M31 19v-3a3 3 0 0 1 6 0v3" stroke="var(--orange)" stroke-width="2" fill="none"/></svg>
  <h3>Seccurity and transparency of purchase</h3>
  <p>Sed eget turpis a pede tempor malesuada. Vivamus quis mi at leo pulvinar hendrerit. Cum sociis natoque penatibus et magnis dis parturient montes.</p></div>

<!-- seller benefits -->
<h2 class="abs section-title" style="top:1391px">Benefits for Oil Seller</h2>
<div class="abs drop-deco" role="img" aria-label="Faint oil drop splash decoration"></div>

<div class="abs card" style="left:234px;top:1498px">
  <svg width="40" height="40" viewBox="0 0 40 40" fill="none" stroke="var(--navy)" stroke-width="2"><circle cx="20" cy="6" r="4"/><circle cx="7" cy="32" r="4"/><circle cx="33" cy="32" r="4"/><path d="M20 10v8M20 18L9 27M20 18l11 9"/></svg>
  <h3>New sale channel</h3>
  <p>Sed eget turpis a pede tempor malesuada. Vivamus quis mi at leo pulvinar hendrerit. Cum sociis natoque penatibus et magnis dis parturient montes dolnisi.</p></div>
<div class="abs card" style="left:524px;top:1498px">
  <svg width="60" height="44" viewBox="0 0 60 44" fill="none" stroke="var(--navy)" stroke-width="2"><circle cx="30" cy="22" r="21" fill="#dfe2e8"/><circle cx="30" cy="16" r="7"/><path d="M18 40c2-8 7-11 12-11s10 3 12 11"/></svg>
  <h3>Attracting new clients</h3>
  <p>Sed eget turpis a pede tempor malesuada. Vivamus quis mi at leo pulvinar hendrerit. Cum sociis natoque penatibus et magnis dis parturient montes, nascet.</p></div>
<div class="abs card" style="left:804px;top:1498px">
  <svg width="40" height="40" viewBox="0 0 40 40" fill="none" stroke="var(--navy)" stroke-width="2"><rect x="6" y="10" width="28" height="26"/><path d="M16 18l5-6 5 6a5 5 0 0 1-10 0z"/><line x1="10" y1="30" x2="30" y2="30"/></svg>
  <h3>More oil sold</h3>
  <p>Sed eget turpis a pede tempor malesuada. Vivamus quis mi at leo pulvinar hendrerit. Cum sociis natoque penatibus et magnis dis parturient montes.</p></div>
<div class="abs card" style="left:366px;top:1781px">
  <svg width="40" height="40" viewBox="0 0 40 40"><path d="M13 16v-5a7 7 0 0 1 14 0v5" stroke="var(--navy)" stroke-width="3" fill="none"/><rect x="9" y="16" width="22" height="22" fill="var(--navy)"/><text x="20" y="33" font-size="13" font-weight="700" fill="#fff" text-anchor="middle" font-family="Open Sans,sans-serif">$</text></svg>
  <h3>Transaction security</h3>
  <p>Sed eget turpis a pede tempor malesuada. Vivamus quis mi at leo pulvinar hendrerit. Cum sociis natoque penatibus et magnis dis parturient montes.</p></div>
<div class="abs card" style="left:656px;top:1781px">
  <svg width="44" height="40" viewBox="0 0 44 40" fill="none" stroke="var(--navy)" stroke-width="2"><text x="22" y="8" font-size="9" fill="var(--navy)" stroke="none" text-anchor="middle" font-family="Open Sans,sans-serif">$ $ $</text><path d="M6 14h32v10a16 14 0 0 1-32 0z"/><path d="M16 20v10M22 20v14M28 20v10"/></svg>
  <h3>Integrate with distribution infrastructure and logistits</h3>
  <p>Sed eget turpis a pede tempor malesuada. Vivamus quis mi at leo pulvinar hendrerit. Cum sociis natoque penatibus et magnis dis parturient montes.</p></div>

<!-- contact -->
<section class="abs band" style="top:2066px;height:627px"></section>
<h2 class="abs section-title" style="top:2132px;font-size:31px">CONTACT US</h2>
<p class="abs contact-lead">Sed eget turpis a pede tempor malesuada. Vivamus quis mi at leo pulvinar hendrerit. Cum sociis natoque penatibus et magnis dis parturient montes dolnisi.</p>

<div class="abs address"><h4>Address</h4>14,Harbour Lane<br>Eastwick,Kent<br>EK4 2QA</div>
<div class="abs info">
  <div><svg width="14" height="14" viewBox="0 0 14 14"><circle cx="7" cy="7" r="6" fill="none" stroke="#333" stroke-width="1.3"/><path d="M4.5 4.5c0 3 2 5 5 5l.6-1.4-1.6-.8-.7.7c-1-.5-1.6-1.1-2-2l.7-.7-.8-1.6z" fill="#333"/></svg>+44 1632 960418</div>
  <div><svg width="14" height="12" viewBox="0 0 14 12"><rect x="1" y="1" width="12" height="10" fill="none" stroke="#333" stroke-width="1.2"/><path d="M1 1l6 5 6-5" fill="none" stroke="#333" stroke-width="1.2"/></svg>hello@crudexa-mail.com</div>
  <div>www.crudexa-trade.com</div>
</div>
<div class="abs connect">Connect with us</div>
<span class="abs social" style="left:290px"></span>
<span class="abs social" style="left:345px"></span>
<span class="abs social" style="left:404px"></span>

<div class="abs field" style="top:2376px;height:29px">Name*</div>
<div class="abs field" style="top:2433px;height:29px">Email*</div>
<div class="abs field" style="top:2484px;height:128px">Message</div>
<a class="abs send">SEND NOW</a>

<footer class="abs footer">@2016crudexa.All rights reserved</footer>
</body>
</html>
```